SirTrim.com.au website design

SirTrim.com.au is a new Australian website selling a monthly supply of razors to men, offering them the convenience of free home delivery and helping them escape the high prices for razors found in supermarkets.

We need a home page as per the details listed below, and the winner will need to design additional pages (a few static pages, product page and checkout page) which will hopefully be easy once the theme on the home page is established

- Home page design that utilises best practice user experience design, intelligent colour theory and colour scheme and a design that achieves the goals of the home page

- The goal of the home page is to communicate how the site works/whats on offer, and convince consumers to buy

- logo

- navigation menu (Home, Buy razors, how it works, contact us)

- Small nav sub-menu (Sign up, Log in, Help)

- three main panels showing three main buying options (2 blade razor $5 per month, 4 blade razor $7 per month, 6 blade razor $9 per month)

- Three sub-panels (Why choose SirTrim.com.au?, Love for SirTrim.com.au - twitter plugin showing tweets from SirTrim, Why pay supermarket prices? See how SirTrim stacks up)

- Footer containing nav menu items + FAQ + Compare prices + Terms and conditions + Privacy Policy, Copyright info, Website security logos and info)

Target Market(s)

Men aged 18-60

Industry/Entity Type

Security

Requirements
Must have
• - Symmetry

- Key info must be above the fold

- Be innovative and really consider how this website will stand out and highlight the key features to consumers
Nice to have
• - Textures are sometimes good
- Maybe the main buying option panels are greyed out and then upon rollover they go to full colour and/or enlarge to highlight the offer in consumers minds?
- Maybe the three main buying option panels are part of a rotating banner?
Should not have
• - Ugly fonts (serif fonts are usually this)

```html
<!DOCTYPE html>
<html lang="en">
<head>
<meta charset="utf-8">
<title>SirTrim.com.au — Home</title>
<link href="https://fonts.googleapis.com/css2?family=Open+Sans:wght@300;400;600&family=Libre+Baskerville:wght@400;700&family=Heebo:wght@300&display=swap" rel="stylesheet">
<style>
  :root {
    --backdrop: #8e8e8e;
    --page: #ffffff;
    --ink: #222222;
    --ink-soft: #555555;
    --ink-muted: #7a7a7a;
    --rule: #d4d4d4;
    --brand-red: #a33333;
    --accent-red: #e01818;
    --more-red: #c00000;
    --hero-bg: #e9e9e7;
    --dot-grey: #6b6b6b;
  }
  * { box-sizing: border-box; margin: 0; padding: 0; }
  html, body { width: 1200px; height: 900px; overflow: hidden; }
  body {
    background: repeating-linear-gradient(90deg, #8a8a8a 0 2px, #959595 2px 4px), var(--backdrop);
    font-family: "Open Sans", Arial, sans-serif;
    color: var(--ink);
    position: relative;
  }
  .page {
    position: absolute; left: 44px; top: 0; width: 1116px; height: 900px;
    background: var(--page);
  }
  .page > * { position: absolute; }

  .logo {
    left: 22px; top: 30px;
    font-family: "Libre Baskerville", Georgia, serif; font-weight: 700;
    font-size: 46px; color: var(--ink); letter-spacing: -1px;
  }

  .shipping { right: 282px; top: 26px; text-align: center; font-family: "Libre Baskerville", Georgia, serif; }
  .shipping-title { font-size: 30px; color: var(--ink); line-height: 1.2; }
  .shipping-sub { font-size: 15px; color: var(--ink-soft); letter-spacing: 1px; margin-top: 2px; }
  .shipping-divider { left: 856px; top: 33px; width: 1px; height: 58px; background: #888; }

  .account-links { left: 919px; top: 8px; display: flex; gap: 25px; font-size: 13px; }
  .account-links a { color: var(--ink); text-decoration: none; }
  .search {
    left: 888px; top: 37px; width: 200px; height: 22px;
    border: 1px solid #777; font-size: 13px; padding: 1px 6px; color: var(--ink);
  }
  .search svg { position: absolute; right: 5px; top: 7px; }
  .cart { left: 985px; top: 73px; font-size: 13px; color: var(--ink-soft); }
  .cart span { color: var(--accent-red); }

  .main-nav {
    left: 0; top: 117px; width: 1114px; height: 41px;
    background: linear-gradient(#ffffff, #ececec);
    border-top: 1px solid var(--rule); border-bottom: 1px solid var(--rule);
    display: flex; justify-content: flex-end; align-items: center; gap: 41px; padding-right: 24px;
  }
  .main-nav a { font-size: 15px; color: #444; text-decoration: none; }

  .hero { left: 0; top: 158px; width: 1116px; height: 322px; background: var(--hero-bg); overflow: hidden; }
  .hero-photo {
    position: absolute; left: 0; top: 0; width: 583px; height: 322px;
    background: linear-gradient(90deg, #d9d7d3 0%, #ecebe8 45%, #cfcfcc 100%);
  }
  .hero-blinds {
    position: absolute; left: 583px; top: 0; width: 533px; height: 322px;
    background: repeating-linear-gradient(180deg, #efefed 0 6px, #e2e2e0 6px 8px);
  }
  .hero-title {
    position: absolute; left: 653px; top: 115px;
    font-family: "Heebo", Arial, sans-serif; font-weight: 300; font-size: 56px; color: #1e1e1e;
  }
  .hero-price { position: absolute; left: 765px; top: 185px; font-size: 22px; color: var(--accent-red); }
  .hero-dots { position: absolute; left: 1002px; top: 291px; display: flex; gap: 11px; }
  .hero-dots span { width: 19px; height: 19px; border-radius: 50%; background: var(--dot-grey); }
  .hero-dots span.is-active { background: var(--brand-red); }

  .brand-band {
    left: 0; top: 480px; width: 1116px; height: 42px; background: var(--brand-red);
    border: 2px solid var(--brand-red); outline: 1px solid #fff; outline-offset: -4px;
    font-family: "Libre Baskerville", Georgia, serif; font-weight: 700; font-size: 20px; color: #fff;
    padding: 7px 16px;
  }

  .panels { left: 6px; top: 551px; display: flex; gap: 12px; }
  .panel {
    position: relative; width: 359px; height: 244px;
    border: 1px solid #c8c8c8; border-radius: 5px; background: #fff;
  }
  .panel-image { position: absolute; left: 10px; top: 10px; width: 96px; height: 88px; border-radius: 3px; }
  .panel-image.is-trimmer { background: linear-gradient(90deg, #d9dde3, #a9c6e6); }
  .panel-image.is-razor { background: linear-gradient(135deg, #e4ecf5, #5a9be0); }
  .panel-image.is-disposables { background: linear-gradient(90deg, #3a4a5c, #9bb5cf); }
  .panel-heading {
    position: absolute; right: 8px; top: 12px; text-align: left; width: 236px;
    font-size: 23px; font-weight: 300; line-height: 33px; color: #222;
  }
  .panel-heading small { display: block; font-size: 23px; }
  .panel-heading.is-compact { font-size: 19px; line-height: 26px; width: 270px; }
  .panel-heading strong { font-weight: 600; }
  .panel-body {
    position: absolute; left: 14px; top: 103px; width: 334px;
    font-size: 13px; line-height: 17.6px; color: var(--ink-muted); text-align: justify;
  }
  .panel-more {
    position: absolute; right: 12px; bottom: 20px;
    font-family: "Libre Baskerville", Georgia, serif; font-size: 16px; color: var(--more-red); text-decoration: none;
  }

  .footer-rule { left: 0; top: 823px; width: 1116px; height: 1px; background: var(--rule); }
  .footer-nav { left: 15px; top: 834px; display: flex; gap: 30px; font-size: 15px; }
  .footer-nav a { color: #444; text-decoration: none; }
  .copyright { left: 15px; top: 868px; font-size: 12px; color: var(--ink-soft); }
  .payment-badges { left: 931px; top: 861px; display: flex; gap: 6px; }
  .payment-badges span {
    width: 54px; height: 30px; border: 1px solid #bbb; border-radius: 2px;
    background: linear-gradient(#ffffff, #e6e6e6);
  }
</style>
</head>
<body>
<div class="page">
  <div class="logo">SirTrim</div>

  <div class="shipping">
    <div class="shipping-title">Free Shipping</div>
    <div class="shipping-sub">ON ORDERS OVER $ 50</div>
  </div>
  <div class="shipping-divider"></div>

  <nav class="account-links">
    <a href="#">Sign up</a><a href="#">Log in</a><a href="#">Help</a>
  </nav>
  <div class="search">Search
    <svg width="5" height="7" viewBox="0 0 5 7"><path d="M0 0 L5 3.5 L0 7 Z" fill="#333"/></svg>
  </div>
  <div class="cart">Cart: <span>(0 items)</span></div>

  <nav class="main-nav">
    <a href="#">Home</a><a href="#">Buy razors</a><a href="#">How it works</a><a href="#">Contact us</a>
  </nav>

  <section class="hero">
    <div class="hero-photo" role="img" aria-label="Photo of a man shaving at a bathroom mirror with a woman beside him"></div>
    <div class="hero-blinds"></div>
    <div class="hero-title">2 Blade Razor</div>
    <div class="hero-price">$5 per month</div>
    <div class="hero-dots"><span class="is-active"></span><span></span><span></span></div>
  </section>

  <div class="brand-band">SirTrim.com.au</div>

  <div class="panels">
    <article class="panel">
      <div class="panel-image is-trimmer" role="img" aria-label="Product photo of a razor and its stand"></div>
      <h2 class="panel-heading">Why choose <small>SirTrim.com.au?</small></h2>
      <p class="panel-body">Your text will go here. Your text will go here. Your text will go here. Your text will go here. Your text will go here. Your text will go here. Your text will go here. Your text will go here. Your text will go here.</p>
      <a class="panel-more" href="#">more info</a>
    </article>
    <article class="panel">
      <div class="panel-image is-razor" role="img" aria-label="Product photo of a blue razor"></div>
      <h2 class="panel-heading">Love for <small>SirTrim.com.au?</small></h2>
      <p class="panel-body">Your text will go here. Your text will go here. Your text will go here. Your text will go here. Your text will go here. Your text will go here. Your text will go here. Your text will go here. Your text will go here.</p>
      <a class="panel-more" href="#">more info</a>
    </article>
    <article class="panel">
      <div class="panel-image is-disposables" role="img" aria-label="Product photo of two disposable razors" style="width:60px"></div>
      <h2 class="panel-heading is-compact">Why pay supermarket prices? See how <strong>SirTrim</strong> stacks up!</h2>
      <p class="panel-body">Your text will go here. Your text will go here. Your text will go here. Your text will go here. Your text will go here. Your text will go here. Your text will go here. Your text will go here. Your text will go here.</p>
      <a class="panel-more" href="#">more info</a>
    </article>
  </div>

  <div class="footer-rule"></div>
  <nav class="footer-nav">
    <a href="#">Home</a><a href="#">Buy razors</a><a href="#">How it works</a><a href="#">Contact us</a><a href="#">FAQ</a><a href="#">Compare prices</a><a href="#">Terms and conditions</a><a href="#">Privacy Policy</a>
  </nav>
  <div class="copyright">Copyright © 2012 SirTrim.com.au</div>
  <div class="payment-badges" aria-label="Accepted payment methods"><span></span><span></span><span></span></div>
</div>
</body>
</html>
```